Revamp our website

Our website needs a bit of a makeover as it is quite simple and not very interactive. Specific pages we would like to see renewed is the home page (www.lunarkpower.com.au) , solutions top page (https://www.lunarkpower.com.au/solutions/) and a detailed solution page (https://www.lunarkpower.com.au/tesko-retail-final/)

The colour data lines are key to our branding and must be used (happy to see them being used in different ways).

```html
<!DOCTYPE html>
<html lang="en">
<head>
<meta charset="utf-8">
<title>Lunark Power – Home</title>
<link href="https://fonts.googleapis.com/css2?family=Poppins:wght@300;400;500;600&display=swap" rel="stylesheet">
<style>
:root{
  --red:#cf1b42;
  --red-dark:#b3133a;
  --ink:#222;
  --muted:#777;
  --light:#f5f5f5;
  --line:#e4e4e4;
  --white:#fff;
}
*{box-sizing:border-box;margin:0;padding:0}
html,body{width:1200px;height:3879px;overflow:hidden}
body{font-family:'Poppins',sans-serif;color:var(--ink);background:var(--white);position:relative}
.section{position:absolute;left:0;width:1200px}
.center{text-align:center}
.eyebrow{font-size:12px;letter-spacing:2px;color:var(--red);text-transform:uppercase;text-align:center}
.title{font-size:30px;font-weight:500;text-align:center;color:var(--ink);margin-top:6px}
.title-rule{width:110px;height:2px;background:var(--red);margin:12px auto 0;opacity:.6}
.lead{font-size:13px;color:var(--muted);line-height:1.75;text-align:center;width:720px;margin:20px auto 0}
.btn{display:inline-block;font-size:11px;letter-spacing:1px;text-transform:uppercase;padding:9px 18px;font-weight:500}
.btn-red{background:var(--red);color:var(--white)}
.btn-white{background:var(--white);color:var(--red)}
.btn-outline{border:1px solid var(--red);color:var(--red);background:var(--white)}

/* hero */
.hero{top:0;height:520px;background:linear-gradient(160deg,#3d4a5c,#1e2430 60%,#2a2f3a)}
.hero-nav{position:absolute;top:26px;left:40px;right:40px;height:40px;display:flex;align-items:center}
.brand{font-size:46px;font-weight:500;color:var(--white);letter-spacing:-1px}
.menu{margin-left:auto;display:flex;gap:34px;align-items:center;font-size:12px;color:var(--white);text-transform:uppercase;letter-spacing:.5px}
.menu .active{color:var(--red)}
.menu .quote{background:var(--red);padding:9px 12px}
.hero-title{position:absolute;top:208px;width:100%;text-align:center;color:var(--white);font-size:38px;font-weight:500}
.hero-text{position:absolute;top:272px;width:100%;text-align:center;color:#ddd;font-size:13px;line-height:1.75}
.hero-actions{position:absolute;top:348px;width:100%;display:flex;justify-content:center;gap:14px}
.hero-actions .phone{border:1px solid rgba(255,255,255,.7);color:var(--white);display:flex;align-items:center;gap:6px}
.hero-down{position:absolute;top:470px;left:592px}

/* solutions */
.solutions{top:520px;height:570px;background:var(--light)}
.solutions .eyebrow{margin-top:64px}
.cards3{position:absolute;top:217px;left:155px;display:flex;gap:20px}
.sol-card{width:283px;height:293px;background:var(--white);box-shadow:0 2px 8px rgba(0,0,0,.06);text-align:center;padding-top:36px}
.sol-card .icon{width:86px;height:86px;border-radius:50%;background:var(--red);margin:0 auto;display:flex;align-items:center;justify-content:center}
.sol-card h3{font-size:15px;font-weight:500;margin-top:24px}
.sol-card p{font-size:12px;color:var(--muted);line-height:1.6;width:200px;margin:8px auto 0}
.sol-card .arrow{margin-top:16px;color:var(--red);font-size:16px}
.sol-card.featured{background:var(--red);color:var(--white)}
.sol-card.featured .icon{background:var(--white)}
.sol-card.featured p,.sol-card.featured .arrow{color:#fbe3e8}

/* welcome */
.welcome{top:1090px;height:345px;background:var(--white)}
.welcome .eyebrow{margin-top:68px}
.welcome .btn{position:absolute;top:244px;left:536px}

/* products */
.products{top:1435px;height:626px;background:var(--light)}
.products .eyebrow{margin-top:60px}
.prod-cards{position:absolute;top:148px;left:155px;display:flex;gap:20px}
.prod-card{width:283px;height:336px;background:var(--white);text-align:center;box-shadow:0 2px 8px rgba(0,0,0,.06)}
.prod-card .photo{height:176px}
.prod-card h3{font-size:15px;font-weight:500;margin-top:20px}
.prod-card p{font-size:12px;color:var(--muted);line-height:1.6;width:220px;margin:8px auto 0}
.prod-card .arrow{margin-top:10px;color:var(--red);font-size:16px}
.prod-card.featured{background:var(--red);color:var(--white)}
.prod-card.featured p,.prod-card.featured .arrow{color:#fbe3e8}
.pager{position:absolute;left:0;width:1200px;display:flex;justify-content:center;align-items:center;gap:26px;color:var(--red);font-size:16px}

/* team */
.team{top:2061px;height:582px;background:var(--white)}
.team .eyebrow{margin-top:64px}
.members{position:absolute;top:147px;left:155px;display:flex;gap:21px}
.member{width:207px;text-align:center}
.member .portrait{height:215px}
.member h4{font-size:14px;font-weight:500;margin-top:18px}
.member span{font-size:11px;color:var(--muted)}
.member.active{box-shadow:0 4px 14px rgba(0,0,0,.12);height:300px}
.member.active h4{color:var(--red)}

/* banner */
.banner{top:2643px;height:465px;background:linear-gradient(120deg,#5b4a3c,#2f2a28 55%,#6e5b4a)}
.banner-box{position:absolute;left:240px;top:72px;width:720px;height:326px;background:rgba(255,255,255,.86);text-align:center;padding-top:46px}
.banner-box h2{font-size:30px;font-weight:500;color:var(--red)}
.banner-box p{font-size:13px;color:#444;line-height:1.7;width:600px;margin:20px auto 0}
.banner-box .btn{margin-top:42px}

/* philosophy */
.philosophy{top:3108px;height:417px;background:var(--white)}
.philosophy .eyebrow{margin-top:64px}
.philosophy .lead{width:680px;margin-top:24px}
.quote-name{text-align:center;color:var(--red);font-size:14px;font-weight:500;margin-top:28px}
.quote-role{text-align:center;font-size:12px;color:var(--ink)}
.dots{display:flex;justify-content:center;gap:8px;margin-top:16px}
.dots i{width:7px;height:7px;border-radius:50%;background:#ddd}
.dots i.on{background:var(--red)}
.avatar{position:absolute;border-radius:50%;background:linear-gradient(135deg,#b9a79a,#6d5d55)}

/* newsletter + footer */
.newsletter{top:3525px;height:290px;background:var(--red);color:var(--white);text-align:center}
.newsletter h2{font-size:30px;font-weight:500;margin-top:38px}
.signup{display:flex;justify-content:center;margin-top:20px}
.signup .field{width:360px;height:36px;background:var(--white);color:#999;font-size:12px;text-align:left;padding:10px 16px;border-right:1px solid #eee}
.signup .send{height:36px;background:var(--white);color:var(--red);font-size:12px;padding:10px 18px;font-weight:500}
.foot-nav{display:flex;justify-content:center;gap:38px;font-size:11px;text-transform:uppercase;margin-top:40px}
.foot-nav .active{text-decoration:underline}
.foot-contact{font-size:12px;margin-top:24px}
.foot-contact span{margin:0 18px}
.bottom-bar{top:3815px;height:64px;background:var(--white);display:flex;align-items:center;padding:0 40px;font-size:11px;color:var(--muted)}
.bottom-bar .co{color:var(--red)}
.social{margin-left:auto;display:flex;align-items:center;gap:10px}
.social i{width:30px;height:30px;background:var(--red);display:block}
.up{margin-left:120px;color:var(--red);font-size:16px}
</style>
</head>
<body>

<header class="section hero" role="img" aria-label="Photo of hands typing on a laptop in a dim office">
  <nav class="hero-nav">
    <div class="brand">lunark</div>
    <div class="menu">
      <span class="active">Home</span><span>About Us</span><span>Our Team</span><span>Solutions</span><span>Products</span><span>News</span><span class="quote">Get a Free Quote</span>
    </div>
  </nav>
  <h1 class="hero-title">Fortune favours the Lunark.</h1>
  <p class="hero-text">At Lunark™, we develop software solutions that are specifically designed for<br>the Australian Utilities sector.</p>
  <div class="hero-actions">
    <span class="btn phone"><svg width="12" height="12" viewBox="0 0 24 24"><path fill="#fff" d="M6.6 10.8a15 15 0 006.6 6.6l2.2-2.2a1 1 0 011-.25 11.4 11.4 0 003.6.57 1 1 0 011 1V20a1 1 0 01-1 1A17 17 0 013 4a1 1 0 011-1h3.5a1 1 0 011 1c0 1.25.2 2.45.57 3.57a1 1 0 01-.25 1z"/></svg>+61 3 9000 4821</span>
    <span class="btn btn-white">Explore More</span>
  </div>
  <svg class="hero-down" width="16" height="22" viewBox="0 0 16 22"><path d="M8 2v16M3 13l5 5 5-5" stroke="#fff" stroke-width="2" fill="none"/></svg>
</header>

<section class="section solutions">
  <div class="eyebrow">Solutions</div>
  <h2 class="title">We're Here For You.</h2>
  <div class="title-rule"></div>
  <p class="lead">Specialising in the Australian Utilities sector, we are driven to improve your operations<br>and customer experience through intelligent software.<br><span style="color:var(--red)">Get started with Lunark today.</span></p>
  <div class="cards3">
    <div class="sol-card">
      <div class="icon"><svg width="40" height="40" viewBox="0 0 40 40" fill="none" stroke="#fff" stroke-width="2"><path d="M6 20L20 8l14 12"/><path d="M10 17v15h20V17"/><rect x="17" y="23" width="6" height="9"/></svg></div>
      <h3>Retail</h3>
      <p>Are you looking to improve your bottom line by minimising operational costs...</p>
      <div class="arrow">→</div>
    </div>
    <div class="sol-card featured">
      <div class="icon"><svg width="40" height="40" viewBox="0 0 40 40" fill="none" stroke="#cf1b42" stroke-width="2"><circle cx="20" cy="20" r="14"/><path d="M20 20l6-6"/><circle cx="20" cy="20" r="2" fill="#cf1b42"/></svg></div>
      <h3>Metering Services</h3>
      <p>Do you have missing or incorrect data that is impacting your Service Level Agreements with customers...</p>
      <div class="arrow">→</div>
    </div>
    <div class="sol-card">
      <div class="icon"><svg width="40" height="40" viewBox="0 0 40 40" fill="none" stroke="#fff" stroke-width="2"><path d="M20 14L12 36M20 14l8 22M14 30h12M16 24h8"/><circle cx="20" cy="11" r="3"/><path d="M13 5a10 10 0 000 12M27 5a10 10 0 010 12"/></svg></div>
      <h3>Distribution &amp; Transmission</h3>
      <p>Do you have a complex environment that involves a variety of tariffs at one time...</p>
      <div class="arrow">→</div>
    </div>
  </div>
</section>

<section class="section welcome">
  <div class="eyebrow">What We Do</div>
  <h2 class="title">Welcome To Lunark Power</h2>
  <div class="title-rule"></div>
  <p class="lead">At Lunark™, we develop software solutions that are specifically designed for the Australian Utilities sector.<br>Founded by two industry leaders 15 years ago, we are about making the lives easier for those who work so<br>hard to meet growing business and consumer demands.</p>
  <span class="btn btn-red">Discover More</span>
</section>

<section class="section products">
  <div class="eyebrow">Products</div>
  <h2 class="title">Our Products</h2>
  <div class="title-rule"></div>
  <div class="prod-cards">
    <div class="prod-card">
      <div class="photo" role="img" aria-label="Photo of hands reviewing printed invoices" style="background:linear-gradient(135deg,#cfc7bd,#8a7d70)"></div>
      <h3>Billing</h3>
      <p>Improve and automate your number one business process, no matter how flexible or complex the...</p>
      <div class="arrow">→</div>
    </div>
    <div class="prod-card featured">
      <div class="photo" role="img" aria-label="Photo of a laptop on a desk showing a compliance page" style="background:linear-gradient(135deg,#c9b08a,#5f6a78)"></div>
      <h3>Compliance &amp; Automation</h3>
      <p>Compliance requirements in the Australian market continue to grow in complexity.</p>
      <div class="arrow">→</div>
    </div>
    <div class="prod-card">
      <div class="photo" role="img" aria-label="Photo of a team working over documents at a table" style="background:linear-gradient(135deg,#b8b4ad,#5a5650)"></div>
      <h3>Revenue Assurance</h3>
      <p>Protect your bottom line with Lunark. With the only Australian software products that are dedicated to...</p>
      <div class="arrow">→</div>
    </div>
  </div>
  <div class="pager" style="top:531px"><span>←</span><span class="btn btn-outline">View All</span><span>→</span></div>
</section>

<section class="section team">
  <div class="eyebrow">Team</div>
  <h2 class="title">Meet our team</h2>
  <div class="title-rule"></div>
  <div class="members">
    <div class="member"><div class="portrait" role="img" aria-label="Illustrated portrait of Alan on yellow" style="background:#f2e600"></div><h4>Alan</h4><span>Founder and CEO</span></div>
    <div class="member"><div class="portrait" role="img" aria-label="Illustrated portrait of Grant on blue" style="background:#1f8fdf"></div><h4>Grant</h4><span>Founder and CTO</span></div>
    <div class="member active"><div class="portrait" role="img" aria-label="Illustrated portrait of Paul on teal" style="background:#1e7f76"></div><h4>Paul</h4><span>CCIO</span></div>
    <div class="member"><div class="portrait" role="img" aria-label="Illustrated portrait of Paul H on purple" style="background:#8a2fc9"></div><h4>Paul H</h4><span>GM, Business Development</span></div>
  </div>
  <div class="pager" style="top:494px"><span>←</span><span class="btn btn-outline">View All</span><span>→</span></div>
</section>

<section class="section banner" role="img" aria-label="Photo of people working on a laptop in a café">
  <div class="banner-box">
    <h2>Tesko My Friend, Tesko.</h2>
    <p>Tesko is a suite of products combined to create end-to-end software solutions for Australian utility participants.</p>
    <p style="margin-top:12px">Tesko revolutionises the way you conduct business by bringing greater efficiency and transparency to your day-to-day operations.</p>
    <span class="btn btn-outline">Read More</span>
  </div>
</section>

<section class="section philosophy">
  <div class="eyebrow">Happy Clients</div>
  <h2 class="title">Our Lunark Philosophy.</h2>
  <p class="lead">Lorem Ipsum is simply dummy text of the printing and typesetting industry. Lorem Ipsum has been the industry's standard dummy text ever since the 1500s, when an unknown printer took a galley of type and scrambled it to make a type specimen book. It has survived not only five centuries, but also the leap into electronic typesetting, remaining essentially unchanged.</p>
  <div class="quote-name">Sam Keller</div>
  <div class="quote-role">General Manager, Northway Systems</div>
  <div class="dots"><i></i><i class="on"></i><i></i></div>
  <div class="avatar" role="img" aria-label="Client photo" style="left:98px;top:118px;width:72px;height:72px"></div>
  <div class="avatar" role="img" aria-label="Client photo" style="left:186px;top:208px;width:30px;height:30px"></div>
  <div class="avatar" role="img" aria-label="Client photo" style="left:84px;top:245px;width:60px;height:60px"></div>
  <div class="avatar" role="img" aria-label="Client photo" style="left:246px;top:272px;width:26px;height:26px"></div>
  <div class="avatar" role="img" aria-label="Client photo" style="left:1030px;top:118px;width:72px;height:72px"></div>
  <div class="avatar" role="img" aria-label="Client photo" style="left:984px;top:210px;width:34px;height:34px"></div>
  <div class="avatar" role="img" aria-label="Client photo" style="left:1056px;top:244px;width:60px;height:60px"></div>
  <div class="avatar" role="img" aria-label="Client photo" style="left:928px;top:274px;width:26px;height:26px"></div>
</section>

<footer class="section newsletter">
  <h2>Sign Up Newsletter</h2>
  <div class="signup"><div class="field">Enter Your Email...</div><div class="send">SEND ➤</div></div>
  <div class="foot-nav"><span class="active">Home</span><span>About Us</span><span>Our Team</span><span>Solutions</span><span>Products</span><span>News</span><span>Privacy Policy</span><span>Legal Notices</span></div>
  <div class="foot-contact"><span>Phone: +61 3 9000 4821</span>|<span>Email: <u>info@lunarkpower.com.au</u></span></div>
</footer>

<div class="section bottom-bar">
  <span>© 2018 <span class="co">Lunark Power Pvt Ltd.</span> All Right Reserved</span>
  <div class="social"><span style="margin-right:10px">Get Social:</span><i></i><i></i><i></i><i></i></div>
  <span class="up">↑</span>
</div>

</body>
</html>
```